Payday Lending App Interface Design

Hello, we are building a payday lending application, Lendoro, that lend people money. I have drafted some of the screens that show the functionalities we have at the moment, please find the screens in attachments.
The elements in the screens are placed just to show what should be included in those screens, it's not necessary to follow the same layout. If you have better design ideas, you are very welcomed to show off your talent.
I think what we want is a style guide so that we can apply the same style to any screens that are similar to the ones I attached. We really like
the style as in the attached image called Style.png. We might want something similar - a simple, clean design yet fun and engaging. Customised graphical elements such as icons, illustrations are preferable.
Apart from the attached screens, we might also need a design for the On Board screen and the Login/Sign Up screen too.
Our logo colour is in yellow and black. Perhaps we will have a similar colour theme. I also attached the logo file, icon-Lendoro.png, if you would like to put it in your design.
Please message me if you need further information.
Regards
Target Market(s)
Young people that doesn't have strong income
Look and feel
Each slider illustrates characteristics of the customer's brand and the style your logo design should communicate.

```html
<!DOCTYPE html>
<html lang="en">
<head>
<meta charset="utf-8">
<title>Lendoro – App Interface</title>
<link href="https://fonts.googleapis.com/css2?family=Poppins:wght@300;400;500;600;700&display=swap" rel="stylesheet">
<style>
:root{
  --yellow:#f9d60b;
  --yellow-pale:#f8e79a;
  --olive:#6b5a0c;
  --ink:#111111;
  --grey:#9a9a9a;
  --grey-light:#dedede;
  --bg:#f6f6f6;
  --white:#ffffff;
}
*{box-sizing:border-box;margin:0;padding:0}
html,body{width:1200px;height:1127px;overflow:hidden}
body{background:var(--bg);font-family:'Poppins',sans-serif;color:var(--ink);position:relative}
.abs{position:absolute}
.deco-dot{position:absolute;width:20px;height:20px;border-radius:50%;background:#dddddd}
.deco-sphere{position:absolute;left:1053px;top:-40px;width:176px;height:176px;border-radius:50%;background:radial-gradient(circle at 30% 70%,#ffffff,#e4e4e4 70%,#d4d4d4)}
.app-icon{position:absolute;left:52px;top:109px;width:150px;height:150px;border-radius:32px;background:var(--yellow);box-shadow:0 16px 30px rgba(0,0,0,.12);display:flex;align-items:center;justify-content:center;font-weight:600;font-size:24px;color:var(--ink)}

.phone{position:absolute;width:330px;height:715px;border-radius:40px;background:var(--white);overflow:hidden;box-shadow:0 20px 50px rgba(0,0,0,.10)}
.phone-home{left:53px;top:352px}
.phone-menu{left:422px;top:239px;background:var(--yellow)}
.phone-details{left:794px;top:352px;background:var(--ink)}

.menu-icon{position:absolute;width:18px}
.menu-icon span{display:block;height:2px;background:var(--ink);margin-bottom:5px;border-radius:1px}
.avatar{position:absolute;border-radius:50%;background:linear-gradient(160deg,#6b4a3a,#b03040 70%,#8a2030);box-shadow:0 4px 10px rgba(0,0,0,.2)}
.greeting{position:absolute;font-size:18.5px;font-weight:500;white-space:nowrap}
.timeline-line{position:absolute;left:26px;top:180px;width:1px;height:400px;background:var(--grey-light)}
.step{position:absolute;left:21px;font-size:13.5px;white-space:nowrap;display:flex;align-items:center}
.step::before{content:"";width:6px;height:6px;border:1.2px solid var(--ink);border-radius:50%;background:var(--white);margin-right:19px;margin-left:0}
.step.active::before{background:var(--ink);width:7px;height:7px}
.step-note{position:absolute;left:46px;font-size:9px;color:#b8b8b8;white-space:nowrap}
.task-card{position:absolute;left:42px;top:208px;width:272px;height:117px;border-radius:16px;background:var(--yellow);box-shadow:0 14px 24px rgba(0,0,0,.1);overflow:hidden}
.task-card h3{position:absolute;left:15px;top:13px;font-size:13.6px;font-weight:500;white-space:nowrap}
.task-card p{position:absolute;left:15px;top:35px;font-size:9px;line-height:14px;color:#a08a00;white-space:nowrap}
.btn-dark{position:absolute;left:15px;top:75px;height:25px;padding:0 10px;border-radius:7px;background:var(--ink);color:var(--white);font-size:10px;line-height:25px;white-space:nowrap}
.btn-grey{position:absolute;left:46px;top:454px;width:112px;height:26px;border-radius:7px;background:#c9c9c9;font-size:10px;line-height:26px;text-align:center;box-shadow:0 4px 8px rgba(0,0,0,.1)}
.dot-grid{position:absolute;display:grid;gap:5px}
.dot-grid i{width:3px;height:3px;border-radius:50%;background:var(--white)}

.tab-bar{position:absolute;left:14px;top:653px;width:304px;height:51px;border-radius:26px;background:var(--ink)}
.tab-bar svg{position:absolute;top:17px}
.coin{position:absolute;left:140px;top:623px;width:60px;height:60px;border-radius:50%;background:var(--yellow);display:flex;align-items:center;justify-content:center;box-shadow:0 6px 12px rgba(0,0,0,.15)}

.close-x{position:absolute;left:22px;top:40px}
.drawer-email{position:absolute;left:69px;top:107px;font-size:9.6px;color:#7a6a00}
.drawer-link{position:absolute;left:57px;font-size:13px;font-weight:500;white-space:nowrap}
.drawer-icon{position:absolute;left:27px}
.drawer-foot{position:absolute;left:31px;font-size:13px;font-weight:500}
.version{position:absolute;left:31px;top:649px;display:flex;align-items:center;gap:10px;font-size:13px;font-weight:500}
.version i{display:block;width:26px;height:26px;border-radius:7px;background:var(--yellow);box-shadow:0 4px 8px rgba(0,0,0,.2)}
.layer-dark{position:absolute;left:174px;top:242px;width:200px;height:500px;border-radius:40px 0 0 0;background:var(--olive)}
.layer-pale{position:absolute;left:174px;top:328px;width:200px;height:420px;border-radius:40px 0 0 0;background:var(--yellow-pale)}
.layer-home{position:absolute;left:214px;top:150px;width:330px;height:600px;border-radius:40px 0 0 0;background:var(--white);overflow:hidden}

.details-title{position:absolute;left:0;width:330px;top:36px;text-align:center;color:var(--white);font-size:16px}
.sheet{position:absolute;left:0;top:86px;width:330px;height:629px;background:var(--white);border-radius:40px 40px 0 0}
.handle{position:absolute;left:147px;top:14px;width:36px;height:2px;background:#cfcfcf;border-radius:1px}
.center{position:absolute;left:0;width:330px;text-align:center;white-space:nowrap}
.toggle{position:absolute;left:60px;top:188px;width:210px;height:40px;border-radius:9px;background:var(--white);box-shadow:0 8px 16px rgba(0,0,0,.1);overflow:hidden;font-size:13px;font-weight:500}
.toggle span{position:absolute;top:0;height:40px;line-height:40px;text-align:center}
.activity-list{position:absolute;left:23px;top:306px;width:281px;height:208px;border-radius:12px;background:#f4f4f4}
.activity{position:absolute;left:0;width:281px;height:61px}
.activity.current{background:var(--white);border-radius:12px 0 0 12px;box-shadow:0 10px 18px rgba(0,0,0,.08);width:197px}
.activity .label{position:absolute;left:23px;font-size:11px;font-weight:500}
.activity .date{position:absolute;left:23px;font-size:10px;color:var(--grey)}
.activity .amount{position:absolute;right:19px;font-size:13px;font-weight:600}
.activity.muted{opacity:.35}
.amount-chip{position:absolute;left:197px;top:0;width:84px;height:61px;border-radius:12px;background:var(--yellow);font-size:13px;font-weight:600;line-height:61px;text-align:center;box-shadow:0 8px 14px rgba(0,0,0,.1)}
</style>
</head>
<body>

<div class="deco-sphere"></div>
<div class="deco-dot" style="left:300px;top:124px"></div><div class="deco-dot" style="left:363px;top:124px"></div><div class="deco-dot" style="left:427px;top:124px"></div><div class="deco-dot" style="left:490px;top:124px"></div><div class="deco-dot" style="left:553px;top:124px"></div>
<div class="deco-dot" style="left:300px;top:188px"></div><div class="deco-dot" style="left:363px;top:188px"></div><div class="deco-dot" style="left:427px;top:188px"></div><div class="deco-dot" style="left:490px;top:188px"></div><div class="deco-dot" style="left:553px;top:188px"></div>
<div class="deco-dot" style="left:300px;top:252px"></div><div class="deco-dot" style="left:363px;top:252px"></div>
<div class="deco-dot" style="left:300px;top:315px"></div><div class="deco-dot" style="left:363px;top:315px"></div>
<div class="deco-dot" style="left:1150px;top:900px"></div><div class="deco-dot" style="left:1150px;top:964px"></div><div class="deco-dot" style="left:1150px;top:1027px"></div><div class="deco-dot" style="left:1150px;top:1091px"></div>
<div class="deco-dot" style="left:959px;top:1091px"></div><div class="deco-dot" style="left:1023px;top:1091px"></div><div class="deco-dot" style="left:1086px;top:1091px"></div>

<div class="app-icon">Lendoro</div>

<!-- Home screen -->
<section class="phone phone-home">
  <div class="menu-icon" style="left:21px;top:43px"><span></span><span style="width:12px"></span><span style="width:6px"></span></div>
  <svg class="abs" style="left:251px;top:46px" width="16" height="16" viewBox="0 0 16 16" fill="none" stroke="#111" stroke-width="1.4"><rect x="1" y="1" width="5" height="5" rx="1.5"/><rect x="10" y="1" width="5" height="5" rx="1.5"/><rect x="1" y="10" width="5" height="5" rx="1.5"/><rect x="10" y="10" width="5" height="5" rx="1.5"/></svg>
  <div class="avatar" role="img" aria-label="User profile photo" style="left:272px;top:32px;width:40px;height:40px"></div>
  <div class="greeting" style="left:21px;top:100px">Hi, Maya Lorne!</div>
  <div class="timeline-line"></div>
  <div class="step" style="top:163px">Start</div>
  <div class="step active" style="top:219px"></div>
  <div class="task-card">
    <h3>Upload Your Personal Information</h3>
    <p>It Seems Like Your Id Documents Are Expired.<br>Upload Your Document Again To Get Qualified.</p>
    <div class="btn-dark">Upload And Submit</div>
    <div class="dot-grid" style="left:233px;top:77px;grid-template-columns:repeat(5,3px)"><i></i><i></i><i></i><i></i><i></i><i></i><i></i><i></i><i></i><i></i><i></i><i></i><i></i><i></i><i></i><i></i><i></i><i></i><i></i><i></i><i></i><i></i><i></i><i></i><i></i></div>
  </div>
  <div class="step" style="top:358px">Connect Bank Account</div>
  <div class="step" style="top:404px">Apply A Loan</div>
  <div class="step-note" style="top:428px">Get Your Loan That Fit To Your Need</div>
  <div class="btn-grey">Apply Now</div>
  <div class="step" style="top:508px">Repayments</div>
  <div class="step" style="top:564px">Loan Closed</div>
  <div class="tab-bar">
    <svg style="left:35px" width="17" height="17" viewBox="0 0 17 17"><path d="M1 8 8.5 1 16 8v8H1z" fill="#fff"/></svg>
    <svg style="left:96px" width="17" height="17" viewBox="0 0 17 17" fill="none" stroke="#fff" stroke-width="1.4"><rect x="1" y="3" width="15" height="12" rx="2"/><path d="M1 7h15M3 1h11"/></svg>
    <svg style="left:197px" width="18" height="17" viewBox="0 0 18 17" fill="none" stroke="#fff" stroke-width="1.4"><path d="M1 6 9 1l8 5H1zM3 7v7M7 7v7M11 7v7M15 7v7M1 16h16"/></svg>
    <svg style="left:258px" width="17" height="17" viewBox="0 0 17 17" fill="none" stroke="#fff" stroke-width="1.4"><rect x="1" y="3" width="15" height="13" rx="2"/><path d="M1 7h15M5 1v4M12 1v4"/></svg>
  </div>
  <div class="coin"><svg width="30" height="30" viewBox="0 0 30 30" fill="none" stroke="#111" stroke-width="1.4"><circle cx="15" cy="15" r="13"/><path d="M18.5 11c-.5-1.5-2-2.2-3.5-2.2s-3.3.8-3.3 2.6c0 3.8 7 2 7 5.8 0 1.8-1.7 2.8-3.7 2.8s-3.3-.9-3.7-2.4M15 6.5v17"/></svg></div>
</section>

<!-- Side menu screen -->
<section class="phone phone-menu">
  <svg class="close-x" width="16" height="16" viewBox="0 0 16 16" stroke="#111" stroke-width="1.6"><path d="M1 1l14 14M15 1 1 15"/></svg>
  <div class="avatar" role="img" aria-label="User profile photo" style="left:21px;top:84px;width:40px;height:40px;border:2px solid #fff"></div>
  <div class="greeting" style="left:69px;top:83px">Hi, Maya Lorne!</div>
  <div class="drawer-email">maya.lorne@example.com</div>

  <svg class="drawer-icon" style="top:177px" width="18" height="17" viewBox="0 0 18 17" fill="none" stroke="#111" stroke-width="1.3"><path d="M1 6 9 1l8 5H1zM3 7v7M7 7v7M11 7v7M15 7v7M1 16h16"/></svg>
  <div class="drawer-link" style="top:177px">Loan Products</div>
  <svg class="drawer-icon" style="top:228px" width="18" height="16" viewBox="0 0 18 16" fill="none" stroke="#111" stroke-width="1.3"><rect x="1" y="1" width="16" height="14" rx="3"/><path d="M1 8h5l1 2h4l1-2h5"/></svg>
  <div class="drawer-link" style="top:226px">Loan History</div>
  <svg class="drawer-icon" style="left:25px;top:275px" width="20" height="20" viewBox="0 0 20 20" fill="none" stroke="#111" stroke-width="1.3"><circle cx="10" cy="10" r="9"/><path d="M10 9v6M10 5.5v1"/></svg>
  <div class="drawer-link" style="top:275px">Q &amp; A</div>

  <div class="drawer-foot" style="top:563px">Contact Us</div>
  <div class="drawer-foot" style="top:599px">Terms &amp; Conditions</div>
  <div class="version"><i></i>Lendoro V.1.0</div>

  <div class="layer-dark"></div>
  <svg class="abs" style="left:198px;top:286px" width="8" height="13" viewBox="0 0 8 13" fill="none" stroke="#fff" stroke-width="1.4"><path d="M7 1 1 6.5 7 12"/></svg>
  <div class="layer-pale">
    <div class="dot-grid" style="left:4px;top:158px;grid-template-columns:repeat(2,3px);gap:13px 12px"><i style="background:#e3cf6a"></i><i style="background:#e3cf6a"></i><i style="background:#e3cf6a"></i><i style="background:#e3cf6a"></i><i style="background:#e3cf6a"></i><i style="background:#e3cf6a"></i><i style="background:#e3cf6a"></i><i style="background:#e3cf6a"></i><i style="background:#e3cf6a"></i><i style="background:#e3cf6a"></i></div>
    <div class="abs" style="left:23px;top:260px;font-size:13.5px;color:#8a7a30">Ac</div>
  </div>
  <div class="layer-home">
    <div class="menu-icon" style="left:21px;top:44px"><span></span><span style="width:12px"></span><span style="width:6px"></span></div>
    <div class="greeting" style="left:21px;top:101px">Hi, Maya Lorne!</div>
    <div class="timeline-line"></div>
    <div class="step" style="top:164px">Start</div>
    <div class="step active" style="top:220px"></div>
    <div class="task-card" style="top:209px">
      <h3>Upload Your Personal Information</h3>
      <p>It Seems Like Your Id Documents Are Expired.<br>Upload Your Document Again To Get Qualified.</p>
      <div class="btn-dark">Upload And Submit</div>
    </div>
    <div class="step" style="top:359px">Connect Bank Account</div>
    <div class="step" style="top:405px">Apply A Loan</div>
    <div class="step-note" style="top:429px">Get Your Loan That Fit To Your Need</div>
    <div class="btn-grey" style="top:455px">Apply Now</div>
    <div class="step" style="top:509px">Repayments</div>
  </div>
</section>

<!-- Loan details screen -->
<section class="phone phone-details">
  <svg class="abs" style="left:23px;top:42px" width="8" height="13" viewBox="0 0 8 13" fill="none" stroke="#fff" stroke-width="1.5"><path d="M7 1 1 6.5 7 12"/></svg>
  <div class="details-title">Loan Details</div>
  <svg class="abs" style="left:291px;top:41px" width="16" height="16" viewBox="0 0 16 16" fill="none" stroke="#fff" stroke-width="1.4"><rect x="1" y="1" width="5" height="5" rx="1.5"/><rect x="10" y="1" width="5" height="5" rx="1.5"/><rect x="1" y="10" width="5" height="5" rx="1.5"/><rect x="10" y="10" width="5" height="5" rx="1.5"/></svg>
  <div class="sheet">
    <div class="handle"></div>
    <div class="center" style="top:38px;font-size:18.5px;font-weight:500">Next Payment</div>
    <div class="center" style="top:70px;font-size:38px;font-weight:700;letter-spacing:1px">$XX</div>
    <div class="center" style="top:130px;font-size:17.5px;font-weight:600"><span style="color:var(--grey);font-weight:400">On</span> 4 Dec</div>
    <div class="dot-grid" style="left:6px;top:82px;grid-template-columns:repeat(2,4px);gap:12px 12px"><i style="background:#ddd;width:4px;height:4px"></i><i style="background:#ddd;width:4px;height:4px"></i><i style="background:#ddd;width:4px;height:4px"></i><i style="background:#ddd;width:4px;height:4px"></i><i style="background:#ddd;width:4px;height:4px"></i><i style="background:#ddd;width:4px;height:4px"></i><i style="background:#ddd;width:4px;height:4px"></i><i style="background:#ddd;width:4px;height:4px"></i><i style="background:#ddd;width:4px;height:4px"></i><i style="background:#ddd;width:4px;height:4px"></i></div>
    <div class="dot-grid" style="left:306px;top:82px;grid-template-columns:repeat(2,4px);gap:12px 12px"><i style="background:#ddd;width:4px;height:4px"></i><i style="background:#ddd;width:4px;height:4px"></i><i style="background:#ddd;width:4px;height:4px"></i><i style="background:#ddd;width:4px;height:4px"></i><i style="background:#ddd;width:4px;height:4px"></i><i style="background:#ddd;width:4px;height:4px"></i><i style="background:#ddd;width:4px;height:4px"></i><i style="background:#ddd;width:4px;height:4px"></i><i style="background:#ddd;width:4px;height:4px"></i><i style="background:#ddd;width:4px;height:4px"></i></div>
    <div class="toggle">
      <span style="left:0;width:129px;background:var(--ink);color:#fff;border-radius:9px 0 0 9px">XXX</span>
      <span style="left:129px;width:81px">XXX</span>
    </div>
    <div class="abs" style="left:23px;top:263px;font-size:13.6px;font-weight:500">Activities</div>
    <div class="activity-list">
      <div class="activity current" style="top:0">
        <div class="label" style="top:15px">Repaymet</div>
        <div class="date" style="top:32px">Dd Mm Yy</div>
      </div>
      <div class="amount-chip">$ 1,000</div>
      <div class="activity muted" style="top:80px">
        <div class="label" style="top:8px">Repaymet</div>
        <div class="date" style="top:25px">Dd Mm Yy</div>
        <div class="amount" style="top:12px">$ 1,000</div>
      </div>
      <div class="activity muted" style="top:140px">
        <div class="label" style="top:8px">Repaymet</div>
        <div class="date" style="top:25px">Dd Mm Yy</div>
        <div class="amount" style="top:12px">$ 1,000</div>
      </div>
    </div>
  </div>
  <div class="tab-bar">
    <svg style="left:35px" width="17" height="17" viewBox="0 0 17 17" fill="none" stroke="#fff" stroke-width="1.4"><path d="M1 8 8.5 1 16 8v8H1z"/></svg>
    <svg style="left:96px" width="17" height="17" viewBox="0 0 17 17" fill="none" stroke="#fff" stroke-width="1.4"><rect x="1" y="3" width="15" height="12" rx="2"/><path d="M1 7h15M3 1h11"/></svg>
    <svg style="left:197px" width="18" height="17" viewBox="0 0 18 17" fill="none" stroke="#fff" stroke-width="1.4"><path d="M1 6 9 1l8 5H1zM3 7v7M7 7v7M11 7v7M15 7v7M1 16h16"/></svg>
    <svg style="left:258px" width="17" height="17" viewBox="0 0 17 17" fill="none" stroke="#fff" stroke-width="1.4"><rect x="1" y="3" width="15" height="13" rx="2"/><path d="M1 7h15M5 1v4M12 1v4"/></svg>
  </div>
  <div class="coin"><svg width="30" height="30" viewBox="0 0 30 30" fill="none" stroke="#111" stroke-width="1.4"><circle cx="15" cy="15" r="13"/><path d="M18.5 11c-.5-1.5-2-2.2-3.5-2.2s-3.3.8-3.3 2.6c0 3.8 7 2 7 5.8 0 1.8-1.7 2.8-3.7 2.8s-3.3-.9-3.7-2.4M15 6.5v17"/></svg></div>
</section>

</body>
</html>
```